Brightmoor Dental Care Stationery

create stationery, business cards and envelops for business. Use current logo on website but open to new fonts for the business name. Business name is Brightmoor Dental Care, would like below the name added "Cosmetic - Family - Implants" Website is www.brightmoordentalcareXQ.example. I would like to have modern look, clean, and professional. The water mark of the logo is a great thing to ad as well.

Target Market(s)

General public, Families, Cosmetic, Implant

Industry/Entity Type

Dental

Font styles to use
Sans Serif

Colors
9bcb3c
000000
757575
c9c9c9

Requirements
Must have
• Would like to see different versions of the current logo. Improvements, color, sytle, and class.
Nice to have
• current font has double "oo" in the Brightmoor logo, does not need to have with new logo.

```html
<!DOCTYPE html>
<html lang="en">
<head>
<meta charset="utf-8">
<title>Brightmoor Dental Care Stationery</title>
<link rel="stylesheet" href="https://fonts.googleapis.com/css2?family=Roboto:wght@400;500;700&display=swap">
<style>
  :root {
    --green: #9bcb3c;
    --charcoal: #333333;
    --black: #1f1f1f;
    --grey: #757575;
    --light: #c9c9c9;
    --white: #ffffff;
    --table: #e6e9ea;
  }
  * { box-sizing: border-box; margin: 0; padding: 0; }
  html, body { width: 1200px; height: 1200px; overflow: hidden; }
  body { font-family: "Roboto", Arial, sans-serif; background: var(--white); position: relative; }

  .letterhead-band {
    position: absolute; left: 0; top: 0; width: 1200px; height: 212px;
    background: var(--charcoal); border-bottom: 5px solid var(--green);
  }
  .brand { position: absolute; display: flex; align-items: center; gap: 14px; }
  .brand-ring { border-radius: 50%; border: 4px solid var(--green); flex: none; }
  .brand-name { font-weight: 700; line-height: 1.1; }
  .brand-tagline { font-weight: 500; letter-spacing: 0.04em; text-transform: uppercase; }

  .letterhead-band .brand { left: 86px; top: 48px; }
  .letterhead-band .brand-ring { width: 100px; height: 100px; }
  .letterhead-band .brand-name { color: var(--white); font-size: 30px; }
  .letterhead-band .brand-tagline { color: var(--white); font-size: 12px; margin-top: 12px; }

  .letterhead-contact {
    position: absolute; left: 826px; top: 32px; color: var(--white);
    text-transform: uppercase; letter-spacing: 0.05em;
  }
  .letterhead-contact .doctor { font-size: 27px; font-weight: 500; margin-bottom: 8px; }
  .letterhead-contact p { font-size: 16px; font-weight: 500; line-height: 31px; }

  .card-table {
    position: absolute; left: 0; top: 411px; width: 1200px; height: 789px;
    background: var(--table);
  }
  .business-card {
    position: absolute; width: 500px; height: 286px; top: 250px;
    box-shadow: 0 6px 18px rgba(0,0,0,0.15); text-transform: uppercase;
  }
  .card-light { left: 70px; background: var(--white); color: var(--black); }
  .card-dark { left: 630px; background: var(--black); color: var(--white); }

  .card-name { position: absolute; left: 30px; top: 30px; }
  .card-name .doctor { font-size: 19px; font-weight: 700; letter-spacing: 0.04em; }
  .card-name .specialties { font-size: 11px; font-weight: 500; letter-spacing: 0.05em; margin-top: 3px; }

  .business-card .brand { left: 120px; top: 100px; }
  .business-card .brand-ring { width: 64px; height: 64px; border-width: 3px; }
  .business-card .brand-name { font-size: 20px; }
  .card-light .brand-name { color: var(--grey); }

  .card-address {
    position: absolute; right: 28px; top: 190px; text-align: right;
    font-size: 11px; font-weight: 500; line-height: 16px; letter-spacing: 0.04em;
  }
  .card-contact { position: absolute; left: 30px; bottom: 24px; font-size: 11px; font-weight: 500; letter-spacing: 0.04em; }
  .card-contact li { list-style: none; display: flex; align-items: center; gap: 10px; height: 22px; }
  .card-contact svg { width: 18px; height: 18px; }
</style>
</head>
<body>

<header class="letterhead-band">
  <div class="brand">
    <span class="brand-ring"></span>
    <div>
      <div class="brand-name">Brightmoor<br>Dental Care</div>
      <div class="brand-tagline">Cosmetic - Family - Implants</div>
    </div>
  </div>
  <div class="letterhead-contact">
    <div class="doctor">Dr. Marcus Ellery</div>
    <p>1280 N Harlow Ave</p>
    <p>Fairhaven, XQ 00000-1234</p>
    <p>www.brightmoordentalcareXQ.example</p>
    <p>555-014-2738</p>
  </div>
</header>

<section class="card-table">
  <article class="business-card card-light">
    <div class="card-name">
      <div class="doctor">Dr. Marcus Ellery</div>
      <div class="specialties">Cosmetic - Family - Implants</div>
    </div>
    <div class="brand">
      <span class="brand-ring"></span>
      <div class="brand-name">Brightmoor<br>Dental Care</div>
    </div>
    <div class="card-address">1280 N Harlow Ave<br>Fairhaven, XQ 00000-1234<br>www.brightmoordentalcareXQ.example</div>
    <ul class="card-contact">
      <li><svg viewBox="0 0 20 20"><circle cx="10" cy="10" r="8.5" fill="none" stroke="currentColor" stroke-width="1.5"/><path d="M7 6c-1 1-1 3 1 5s4 3 5 2l-1.5-1.5-1 .6-2.5-2.5.6-1z" fill="currentColor"/></svg>555-014-2738</li>
      <li><svg viewBox="0 0 20 20"><rect x="2" y="5" width="16" height="11" fill="none" stroke="currentColor" stroke-width="1.5"/><path d="M2 5l8 6 8-6" fill="none" stroke="currentColor" stroke-width="1.5"/></svg>hello@brightmoor.example</li>
    </ul>
  </article>

  <article class="business-card card-dark">
    <div class="card-name">
      <div class="doctor">Dr. Marcus Ellery</div>
      <div class="specialties">Cosmetic - Family - Implants</div>
    </div>
    <div class="brand">
      <span class="brand-ring"></span>
      <div class="brand-name">Brightmoor<br>Dental Care</div>
    </div>
    <div class="card-address">1280 N Harlow Ave<br>Fairhaven, XQ 00000-1234<br>www.brightmoordentalcareXQ.example</div>
    <ul class="card-contact">
      <li><svg viewBox="0 0 20 20"><circle cx="10" cy="10" r="8.5" fill="none" stroke="currentColor" stroke-width="1.5"/><path d="M7 6c-1 1-1 3 1 5s4 3 5 2l-1.5-1.5-1 .6-2.5-2.5.6-1z" fill="currentColor"/></svg>555-014-2738</li>
      <li><svg viewBox="0 0 20 20"><rect x="2" y="5" width="16" height="11" fill="none" stroke="currentColor" stroke-width="1.5"/><path d="M2 5l8 6 8-6" fill="none" stroke="currentColor" stroke-width="1.5"/></svg>hello@brightmoor.example</li>
    </ul>
  </article>
</section>

</body>
</html>
```